Home loan company

looking for a simple and professional looking website. Front page will have a map of Australia with several counters. Need to. Be able to register interest name ,contact, dollar amount ect. This info must be placed into a data base .

We have a logo , colour scheme and an in depth outline that will be sent to interested People.

Industry/Entity Type

Loan

Number of Pages Required

5+ page

```html
<!DOCTYPE html>
<html lang="en">
<head>
<meta charset="utf-8">
<title>Team Southland Home Loan</title>
<link href="https://fonts.googleapis.com/css2?family=Oswald:wght@300;400;500&family=Open+Sans:wght@400;600&display=swap" rel="stylesheet">
<style>
:root{
  --green:#22a82a;
  --green-bright:#3ddc3a;
  --red:#c70d0d;
  --page:#1b1b1b;
  --footer:#2a2a2a;
  --card:#e4e4e4;
  --panel:#ffffff;
  --form-bg:#f4f4f4;
  --band-light:#e6e6e6;
  --band-dark:#6e6e6e;
  --ink:#111111;
  --muted:#555555;
  --digit:#2b2b2b;
  --white:#ffffff;
}
*{box-sizing:border-box;margin:0;padding:0}
html,body{width:1200px;height:905px;overflow:hidden}
body{background:var(--page);font-family:'Open Sans',sans-serif;color:var(--ink);position:relative}

.site-header{position:absolute;left:0;top:0;width:1200px;height:156px;background:linear-gradient(#333,#262626);border-bottom:3px solid var(--green-bright)}
.brand{position:absolute;left:76px;top:58px;display:flex;align-items:center;gap:12px}
.brand-mark{width:30px;height:30px;background:var(--green-bright)}
.brand-name{font-family:'Oswald',sans-serif;font-weight:400;color:var(--white);font-size:26px;line-height:32px;white-space:nowrap}

.counter{position:absolute;left:451px;top:32px}
.counter-label{color:#eee;font-size:18px;margin-bottom:10px}
.counter-digits{display:flex;gap:4px;padding:5px;background:#3a3a3a;border-radius:4px;border:1px solid #4a4a4a}
.counter-digits span{width:36px;height:48px;background:linear-gradient(#5a5a5a,var(--digit) 50%,#1e1e1e 50%,#3a3a3a);color:#fff;font-family:'Oswald',sans-serif;font-size:34px;line-height:48px;text-align:center;border-radius:3px}

.countdown{position:absolute;left:924px;top:14px;width:220px;text-align:center;font-family:'Oswald',sans-serif;color:#fff}
.countdown svg{display:block;margin:0 auto 6px}
.countdown-time{font-size:30px;line-height:34px}
.countdown-time b{color:var(--green-bright);font-weight:400}
.countdown-label{font-size:22px;font-weight:300;line-height:26px}

.action{position:absolute;top:196px;width:138px;height:110px;color:#fff;text-align:center;font-family:'Oswald',sans-serif;font-size:21px;line-height:24px;padding-top:14px;text-decoration:none}
.action svg{display:block;margin:0 auto 6px}
.action-register{left:74px;background:var(--green)}
.action-apply{left:233px;background:var(--red)}

.calculator{position:absolute;left:74px;top:344px;width:297px;height:474px;background:var(--form-bg);border:1px solid #ccc}
.calculator-title{height:61px;background:var(--band-light);font-family:'Oswald',sans-serif;font-weight:400;font-size:26px;padding:12px 16px;color:#222}
.calculator-sub{height:36px;background:var(--band-dark);color:#fff;font-family:'Oswald',sans-serif;font-weight:400;font-size:18px;padding:5px 16px}
.calc-body{padding:10px 17px 0}
.field{height:50px;font-size:14px;color:#333}
.field-row{display:flex;align-items:center;margin-top:4px;font-size:12px;color:#555}
.slider{position:relative;width:159px;height:2px;background:#bbb;margin-right:18px}
.slider i{position:absolute;top:-7px;width:9px;height:16px;background:#111}
.value{border:1px solid #ddd;background:#fff;height:22px;padding:0 6px;font-size:12px;line-height:20px;color:#444;margin-right:8px}
.options{display:flex;gap:12px;font-size:12px;color:#555;margin-top:4px}
.options span::before{content:"";display:inline-block;width:10px;height:10px;border:1px solid #999;border-radius:50%;margin-right:5px;vertical-align:-1px}
.submit{position:absolute;left:0;bottom:0;width:100%;height:49px;background:var(--green);color:#fff;border:0;font-family:'Oswald',sans-serif;font-size:18px}

.states{position:absolute;left:408px;top:196px;width:718px;height:630px;background:var(--panel);border-radius:3px}
.state-card{position:absolute;width:214px;height:103px;background:var(--card);text-align:center;padding-top:12px}
.state-name{font-family:'Oswald',sans-serif;font-size:25px;line-height:28px;color:var(--muted)}
.state-name b{font-weight:400;color:var(--green)}
.state-amount{font-family:'Oswald',sans-serif;font-size:25px;line-height:30px;color:var(--ink)}
.state-count{font-size:14px;color:#777;margin-top:4px}
.state-card.is-active{background:var(--green)}
.state-card.is-active *, .state-card.is-active b{color:#fff}
.map{position:absolute;left:264px;top:27px;width:414px;height:335px;background:linear-gradient(135deg,#f6a05c,#f5ee3a 40%,#8ebde2 60%,#f17a5c);border-radius:40% 30% 35% 45%;opacity:.85}

.site-footer{position:absolute;left:0;top:862px;width:1200px;height:43px;background:var(--footer);color:#ccc;font-size:13px;display:flex;align-items:center;justify-content:space-between;padding:0 74px}
.social{display:flex;align-items:center;gap:6px}
.social i{width:22px;height:22px;border:1.5px solid #ccc;border-radius:50%}
</style>
</head>
<body>
<header class="site-header">
  <div class="brand">
    <div class="brand-mark"></div>
    <div class="brand-name">Team Southland Home Loan</div>
  </div>

  <div class="counter">
    <div class="counter-label">Look like a counter</div>
    <div class="counter-digits"><span>9</span><span>8</span><span>8</span><span>2</span><span>8</span><span>7</span><span>9</span><span>7</span><span>8</span><span>8</span></div>
  </div>

  <div class="countdown">
    <svg width="46" height="42" viewBox="0 0 46 42"><circle cx="24" cy="22" r="17" fill="none" stroke="#888" stroke-width="3"/><path d="M24 12v11l7 5" fill="none" stroke="#888" stroke-width="3"/><path d="M4 14l4 6 5-5" fill="none" stroke="#888" stroke-width="3"/></svg>
    <div class="countdown-time"><b>50</b> DAYS <b>10</b> MINS</div>
    <div class="countdown-label">REMAINING</div>
  </div>
</header>

<a class="action action-register" href="#">
  <svg width="30" height="28" viewBox="0 0 30 28"><rect x="3" y="3" width="18" height="22" fill="none" stroke="#fff" stroke-width="2"/><path d="M7 10h10M7 15h8M7 20h6" stroke="#fff" stroke-width="2"/><path d="M17 20l10-14" stroke="#fff" stroke-width="3"/></svg>
  REGISTER<br>INTEREST
</a>
<a class="action action-apply" href="#">
  <svg width="30" height="28" viewBox="0 0 30 28"><circle cx="15" cy="8" r="6" fill="#fff"/><path d="M4 27c0-8 5-12 11-12s11 4 11 12z" fill="#fff"/></svg>
  APPLY<br>ONLINE
</a>

<section class="calculator">
  <h2 class="calculator-title">LOAN REPAYMENTS</h2>
  <h3 class="calculator-sub">MY HOME LOAN</h3>
  <div class="calc-body">
    <div class="field">Loan Amount<div class="field-row"><div class="slider"><i style="left:4px"></i></div><span class="value" style="width:86px">$300,000</span></div></div>
    <div class="field">Loan Period<div class="field-row"><div class="slider"><i style="left:108px"></i></div><span class="value">25</span>Year/s</div></div>
    <div class="field">Loan Type<div class="options"><span>Variable</span><span>Fixed</span></div></div>
    <div class="field" style="height:53px">Interest Rate<div class="field-row"><div class="slider"><i style="left:4px"></i></div><span class="value">6.25</span>% p.a</div></div>
    <div class="field" style="height:52px">Repayment Frequency<div class="options"><span>Monthly</span><span>Fortnightly</span><span>Weekly</span></div></div>
    <div class="field">Repayment Frequency<div class="options"><span>Principal &amp; Interest</span><span>Interest Based</span></div></div>
  </div>
  <button class="submit">SUBMIT</button>
</section>

<main class="states">
  <div class="state-card" style="left:19px;top:19px"><div class="state-name">TEAM <b>NSW</b></div><div class="state-amount">$500,000,000.00</div><div class="state-count">9560 People Registered</div></div>
  <div class="state-card is-active" style="left:19px;top:141px"><div class="state-name">TEAM <b>QLD</b></div><div class="state-amount">$200,000,000.00</div><div class="state-count">9560 People Registered</div></div>
  <div class="state-card" style="left:19px;top:264px"><div class="state-name">TEAM <b>WA</b></div><div class="state-amount">$300,000,000.00</div><div class="state-count">9560 People Registered</div></div>
  <div class="map" role="img" aria-label="Map of Australia with each state coloured and labelled"></div>
  <div class="state-card" style="left:19px;top:385px"><div class="state-name">TEAM <b>SA</b></div><div class="state-amount">$10,000,000.00</div><div class="state-count">9560 People Registered</div></div>
  <div class="state-card" style="left:252px;top:385px"><div class="state-name">TEAM <b>VIC</b></div><div class="state-amount">$200,000,000.00</div><div class="state-count">9560 People Registered</div></div>
  <div class="state-card" style="left:485px;top:385px"><div class="state-name">TEAM <b>RLX</b></div><div class="state-amount">$200,000,000.00</div><div class="state-count">9560 People Registered</div></div>
  <div class="state-card" style="left:19px;top:507px"><div class="state-name">TEAM <b>NT</b></div><div class="state-amount">$50,000,000.00</div><div class="state-count">9560 People Registered</div></div>
  <div class="state-card" style="left:252px;top:507px"><div class="state-name">TEAM <b>TAS</b></div><div class="state-amount">$5,000,000.00</div><div class="state-count">9560 People Registered</div></div>
  <div class="state-card" style="left:485px;top:507px"><div class="state-name">TEAM <b>FBL</b></div><div class="state-amount">$200,000,000.00</div><div class="state-count">9560 People Registered</div></div>
</main>

<footer class="site-footer">
  <span>© 2015 Team Southland Home Loan. All Rights Reserved</span>
  <span class="social">Follow Us On <i></i><i></i></span>
</footer>
</body>
</html>
```